Design Shopify E-Commerce Website for Men's Products

Design a Shopify website for men to sell our men's jewelry, cigar and bar accessories, and other men's products. Design should be hip, with like a rock n' roll, biker, whiskey driker flare. Name of the company is "Outlaw Cupboard" and website will be www.OutlawCupboard.com
Homepage will have navigation bar with three categories: Men's Jewelry, Cigar & Bar Products, Man Cave Swag
I will upload our logo, inspiration type pictures and some of the products that we sell
Theme colors should be mainly dark: black, grey, brown, gold

```html
<!DOCTYPE html>
<html lang="en">
<head>
<meta charset="utf-8">
<title>Outlaw Cupboard — For Legends Only</title>
<link rel="stylesheet" href="https://fonts.googleapis.com/css2?family=UnifrakturCook:wght@700&family=Libre+Baskerville:wght@400;700&family=Arimo:ital,wght@0,400;0,700;1,400&display=swap">
<style>
:root{
  --black:#000;
  --ink:#0b0b0b;
  --panel:#151210;
  --gold:#c49b3c;
  --gold-light:#e8c46a;
  --gold-dark:#9a7428;
  --white:#fff;
  --grey:#bdbdbd;
  --brown:#3a2614;
}
*{box-sizing:border-box;margin:0;padding:0}
html,body{width:1200px;height:4280px;overflow:hidden;background:var(--black);color:var(--white);font-family:"Arimo",Arial,sans-serif}
.page{position:relative;width:1200px;height:4280px}
.abs{position:absolute}
.section-title{position:absolute;left:0;width:1200px;text-align:center;font-family:"UnifrakturCook",serif;font-size:34px;color:var(--gold);letter-spacing:1px}
.rule{position:absolute;left:583px;width:34px;height:4px;background:var(--gold)}
.photo{position:absolute}
.btn-gold{position:absolute;display:flex;align-items:center;justify-content:center;background:linear-gradient(180deg,var(--gold-light),var(--gold) 55%,var(--gold-dark));color:#1a1208;font-family:"Libre Baskerville",serif;font-weight:700;font-size:13px}

/* hero */
.hero{position:absolute;left:0;top:0;width:1200px;height:562px;background:radial-gradient(ellipse at 30% 55%,#6a6a6a 0%,#3a3a3a 35%,#141414 75%,#050505 100%)}
.brand{position:absolute;left:150px;top:34px;display:flex;align-items:center;gap:8px;font-family:"Libre Baskerville",serif;font-size:15px;color:var(--gold)}
.brand .mark{width:18px;height:18px;border-radius:50%;background:var(--gold)}
.nav{position:absolute;left:337px;top:33px;display:flex;height:42px;align-items:center;font-size:11px;background:rgba(0,0,0,.55)}
.nav a{color:var(--white);text-decoration:none;padding:0 20px;line-height:42px}
.nav a.active{background:linear-gradient(180deg,var(--gold-light),var(--gold-dark));padding:0 24px}
.nav-icons{position:absolute;left:940px;top:45px;display:flex;gap:10px}
.hero-kicker{position:absolute;top:183px;width:1200px;text-align:center;font-family:"Libre Baskerville",serif;font-size:17px;color:var(--gold)}
.hero-title{position:absolute;top:198px;width:1200px;text-align:center;font-family:"UnifrakturCook",serif;font-size:86px;color:var(--white);letter-spacing:2px}
.hero-sub{position:absolute;top:313px;width:1200px;text-align:center;font-size:17px;letter-spacing:.5px}
.dots{position:absolute;top:523px;left:584px;display:flex;gap:5px}
.dots i{width:7px;height:7px;border-radius:50%;background:var(--white)}

/* categories */
.cat{position:absolute;top:698px;width:270px;height:322px}
.cat-label{position:absolute;bottom:62px;width:100%;text-align:center;font-family:"UnifrakturCook",serif;font-size:17px}
.cat-btn{position:absolute;bottom:26px;left:62px;width:146px;height:28px;border:1.5px solid var(--gold);display:flex;align-items:center;justify-content:center;font-family:"Libre Baskerville",serif;font-size:12px;color:var(--gold)}

/* about */
.about-box{position:absolute;left:507px;top:1152px;width:530px;height:359px;background:var(--gold)}
.about-title{position:absolute;left:610px;top:1187px;width:390px;text-align:center;font-family:"UnifrakturCook",serif;font-size:34px;color:var(--white);white-space:nowrap}
.about-text{position:absolute;left:615px;top:1252px;width:380px;text-align:center;font-size:10.6px;line-height:20px;color:var(--white)}
.btn-dark{position:absolute;left:715px;top:1426px;width:175px;height:40px;background:#1a1408;color:var(--gold);display:flex;align-items:center;justify-content:center;font-family:"Libre Baskerville",serif;font-size:13px}

/* products */
.products{position:absolute;left:0;top:1600px;width:1200px;height:453px;background:linear-gradient(135deg,#241a10,#0d0a07 45%,#1e150c 80%,#120d08)}
.prod{position:absolute;width:206px}
.prod-img{width:206px;height:175px;background:var(--white);display:flex;align-items:center;justify-content:center}
.prod-name{margin-top:20px;text-align:center;font-family:"Libre Baskerville",serif;font-size:14px;color:var(--gold)}
.prod-price{margin-top:5px;text-align:center;font-size:12px}

/* deal */
.deal-title{position:absolute;left:190px;top:2177px;width:420px;text-align:center;font-family:"UnifrakturCook",serif;font-size:34px;color:var(--gold)}
.deal-text{position:absolute;left:205px;top:2246px;width:385px;text-align:center;font-size:10.6px;line-height:20px}

/* testimonials */
.testi-bg{position:absolute;left:0;top:2581px;width:1200px;height:466px;background:linear-gradient(160deg,#1d1711,#0a0806 55%,#15110c)}
.card{position:absolute;top:2726px;width:411px;height:254px;border-radius:14px;background:#050505;padding:22px 20px}
.card.featured{border:1.5px solid var(--gold)}
.card p{font-style:italic;font-size:11.6px;line-height:22px;color:var(--white)}
.who{position:absolute;left:20px;bottom:16px;display:flex;align-items:center;gap:10px}
.avatar{width:44px;height:44px;border-radius:50%;background:radial-gradient(circle,#6d6d6d,#1b1b1b)}
.who b{display:block;font-family:"Libre Baskerville",serif;font-weight:400;font-size:14px;color:var(--gold)}
.who small{font-style:italic;font-size:9px}
.stars{position:absolute;right:40px;bottom:32px;color:var(--gold);font-size:10px;letter-spacing:1px}
.vdots{position:absolute;left:1061px;top:2813px;display:flex;flex-direction:column;gap:8px}
.vdots i{width:7px;height:7px;border-radius:50%;background:var(--white)}
.vdots i:first-child{background:var(--gold)}

/* social */
.grid{position:absolute;left:163px;top:3208px;width:874px;display:flex;flex-direction:column;gap:5px}
.row{display:flex;gap:5px;height:165px}
.row div{height:165px}

/* newsletter */
.news{position:absolute;left:135px;top:3789px;width:930px;height:150px;border-radius:20px;background:var(--gold)}
.news h2{position:absolute;left:27px;top:28px;font-family:"UnifrakturCook",serif;font-size:32px;font-weight:700;color:var(--white)}
.news p{position:absolute;left:27px;top:92px;width:420px;font-size:10.5px;line-height:19px;color:var(--white)}
.news-input{position:absolute;left:497px;top:30px;width:385px;height:36px;border:1.5px solid var(--white);display:flex;align-items:center;justify-content:center;font-size:11px;color:var(--white)}
.news-btn{position:absolute;left:602px;top:84px;width:176px;height:40px;background:#1a1408;color:var(--gold);display:flex;align-items:center;justify-content:center;font-family:"Libre Baskerville",serif;font-size:13px}

/* footer */
.foot-brand{position:absolute;left:186px;top:4063px;display:flex;align-items:center;gap:10px;font-family:"Libre Baskerville",serif;font-size:20px;color:var(--gold)}
.foot-brand .mark{width:24px;height:24px;border-radius:50%;background:var(--gold)}
.foot-col{position:absolute;top:3982px}
.foot-col h4{font-family:"UnifrakturCook",serif;font-size:15px;color:var(--gold);margin-bottom:16px}
.foot-col li{list-style:none;font-size:10.5px;line-height:22px;display:flex;align-items:center;gap:8px}
.chev{color:var(--gold);font-size:10px}
.icon-dot{width:22px;height:22px;border-radius:50%;background:var(--gold);display:inline-block}
.social li{line-height:33px}
.foot-rule{position:absolute;left:163px;top:4200px;width:874px;height:1px;background:#555}
.copy{position:absolute;top:4219px;width:1200px;text-align:center;font-size:10.5px}
.copy span{font-family:"UnifrakturCook",serif;color:var(--gold)}
</style>
</head>
<body>
<div class="page">

  <!-- HERO -->
  <header class="hero" role="img" aria-label="Black and white photograph of chrome motorcycles parked in a row"></header>
  <div class="brand"><span class="mark"></span>Outlaw Cupboard</div>
  <nav class="nav">
    <a class="active" href="#">Home</a>
    <a href="#">Jewelry</a>
    <a href="#">Cigar &amp; Bar Products</a>
    <a href="#">Legend's Collection</a>
    <a href="#">Contact Us</a>
  </nav>
  <div class="nav-icons">
    <svg width="13" height="13" viewBox="0 0 14 14"><circle cx="6" cy="6" r="4.3" fill="none" stroke="#fff" stroke-width="1.6"/><path d="M9 9l4 4" stroke="#fff" stroke-width="1.8"/></svg>
    <svg width="13" height="13" viewBox="0 0 14 14"><circle cx="7" cy="4" r="3.2" fill="#fff"/><path d="M1 14c0-4 3-6 6-6s6 2 6 6z" fill="#fff"/></svg>
    <svg width="16" height="14" viewBox="0 0 16 14"><path d="M0 1h3l2 8h8l2-6H4" fill="none" stroke="#fff" stroke-width="1.5"/><circle cx="6" cy="12" r="1.3" fill="#fff"/><circle cx="12" cy="12" r="1.3" fill="#fff"/><circle cx="13" cy="2" r="2.5" fill="var(--gold)"/></svg>
  </div>
  <p class="hero-kicker">Welcome to</p>
  <h1 class="hero-title">Outlaw Cupboard</h1>
  <p class="hero-sub">For Legends Only</p>
  <div class="btn-gold" style="left:512px;top:369px;width:176px;height:36px">Shop Our Products</div>
  <div class="dots"><i></i><i></i><i></i><i></i></div>

  <!-- CATEGORIES -->
  <h2 class="section-title" style="top:619px">Categories</h2>
  <div class="rule" style="top:671px"></div>

  <div class="cat" style="left:163px">
    <div class="photo" role="img" aria-label="Close-up of hands wearing silver rings" style="inset:0;background:linear-gradient(160deg,#3a3430,#1a1614 60%,#0c0a09)"></div>
    <div class="cat-label">Jewelry</div>
    <div class="cat-btn">Shop Now</div>
  </div>
  <div class="cat" style="left:465px">
    <div class="photo" role="img" aria-label="Cigars stacked on a wooden surface" style="inset:0;background:linear-gradient(150deg,#6a3e1e,#3b2010 55%,#1a0e06)"></div>
    <div class="abs" style="left:10px;top:12px;right:10px;bottom:12px;border:2px solid var(--gold)"></div>
    <div class="cat-label" style="bottom:78px">Cigar &amp; Bar Products</div>
    <div class="cat-btn" style="bottom:42px">Shop Now</div>
  </div>
  <div class="cat" style="left:768px">
    <div class="photo" role="img" aria-label="Portrait of a bearded man in a grey suit" style="inset:0;background:linear-gradient(180deg,#1e2226,#2c3036 55%,#121416)"></div>
    <div class="cat-label">Legend's Collection</div>
    <div class="cat-btn">Shop Now</div>
  </div>

  <!-- ABOUT -->
  <div class="abs" style="left:156px;top:1092px;width:4px;height:362px;background:var(--gold)"></div>
  <div class="abs" style="left:156px;top:1092px;width:437px;height:4px;background:var(--gold)"></div>
  <div class="photo" role="img" aria-label="Man in a tweed jacket lighting a cigar" style="left:163px;top:1099px;width:430px;height:355px;background:linear-gradient(120deg,#1a1c1e,#3c3a36 50%,#5a4a3a 70%,#1c1a18)"></div>
  <div class="about-box"></div>
  <h2 class="about-title">About Outlaw</h2>
  <div class="abs" style="left:789px;top:1240px;width:34px;height:4px;background:var(--white)"></div>
  <p class="about-text">Lorem ipsum dolor sit amet, consectetur adipiscing elit, sed do eiusmod tempor incididunt ut labore et dolore magna aliqua. Quis ipsum suspendisse ultrices gravida. Risus commodo viverra maecenas accumsan lacus vel facilisis. omnis iste natus error sit voluptatem accusantium doloremque laudantium, totam rem aperiam, eaque ipsa quae ab illo inventore veritatis et quasi architecto beatae vitae dicta sunt explicabo. Nemo enim ipsam voluptatem quia voluptas sit aspernatur aut odit aut fugit, sed quia consequuntur magni dolores voluptatem.</p>
  <div class="btn-dark">Learn More About</div>

  <!-- PRODUCTS -->
  <section class="products" role="img" aria-label="Dim backdrop of stacked cigars"></section>
  <h2 class="section-title" style="top:1668px">Shop Our Products</h2>
  <div class="rule" style="top:1720px"></div>
  <div class="prod" style="left:163px;top:1750px">
    <div class="prod-img"><div role="img" aria-label="Red wooden cigar humidor with glass lid" style="width:150px;height:110px;background:linear-gradient(180deg,#8a2a20,#4a120c)"></div></div>
    <div class="prod-name">Cigar humidor</div><div class="prod-price">$ 120:00</div>
  </div>
  <div class="prod" style="left:386px;top:1750px">
    <div class="prod-img" style="border:3px solid var(--gold)"><div role="img" aria-label="Silver and gold cross signet ring" style="width:120px;height:130px;background:radial-gradient(circle,#c9b06a,#6a6a6a 60%,#2a2a2a)"></div></div>
    <div class="prod-name">Heavy Ring</div><div class="prod-price">$ 120:00</div>
  </div>
  <div class="prod" style="left:608px;top:1750px">
    <div class="prod-img"><div role="img" aria-label="Silver cross pendant" style="width:140px;height:120px;background:radial-gradient(circle,#9a9a9a,#444 70%,#fff 71%)"></div></div>
    <div class="prod-name">Pendant Resized</div><div class="prod-price">$ 120:00</div>
  </div>
  <div class="prod" style="left:831px;top:1750px">
    <div class="prod-img"><div role="img" aria-label="Pair of engraved silver cufflinks" style="width:130px;height:80px;background:radial-gradient(circle,#8a8a8a,#3a3a3a 65%,#fff 66%)"></div></div>
    <div class="prod-name">Cufflinks</div><div class="prod-price">$ 120:00</div>
  </div>

  <!-- DEAL OF THE WEEK -->
  <h2 class="deal-title">Deal of the Week</h2>
  <div class="abs" style="left:380px;top:2235px;width:34px;height:4px;background:var(--gold)"></div>
  <p class="deal-text">Lorem ipsum dolor sit amet, consectetur adipiscing elit, sed do eiusmod tempor incididunt ut labore et dolore magna aliqua. Quis ipsum suspendisse ultrices gravida. Risus commodo viverra maecenas accumsan lacus vel facilisis. omnis iste natus error sit voluptatem accusantium doloremque laudantium, totam rem aperiam, eaque ipsa quae ab illo inventore veritatis et quasi architecto beatae vitae dicta sunt.</p>
  <div class="btn-gold" style="left:304px;top:2378px;width:176px;height:37px">Shop Our Products</div>
  <div class="abs" style="left:651px;top:2098px;width:341px;height:387px;background:var(--gold)"></div>
  <div class="photo" role="img" aria-label="Silver chains, cross pendants and rings laid on a wooden table" style="left:632px;top:2119px;width:335px;height:391px;background:radial-gradient(ellipse at 50% 45%,#a0682a,#6a3e18 60%,#3a2008)"></div>

  <!-- TESTIMONIALS -->
  <div class="testi-bg"></div>
  <h2 class="section-title" style="top:2639px">Testimonials</h2>
  <div class="rule" style="top:2691px"></div>
  <article class="card featured" style="left:176px">
    <p>Lorem ipsum dolor sit amet, consectetur adipiscing elit, sed do eiusmod tempor incididunt ut labore et dolore magna aliqua. Quis ipsum suspendisse ultrices gravida. Risus commodo viverra maecenas accumsan lacus vel facilisis.iste natus error sit voluptatem accusantium doloremque laudantium, totam rem aperiam, eaque ipsa quae ab illo inventore veritatis et quasi architecto beatae vitae dicta sunt explicabo. Nemo enim ipsam voluptatem quia voluptas sit aspernatur aut.</p>
    <div class="who"><div class="avatar" role="img" aria-label="Customer portrait"></div><div><b>-Jack Marlow</b><small>Lorem Ipsum</small></div></div>
    <div class="stars">★★★★★</div>
  </article>
  <article class="card" style="left:613px">
    <p>Lorem ipsum dolor sit amet, consectetur adipiscing elit, sed do eiusmod tempor incididunt ut labore et dolore magna aliqua. Quis ipsum suspendisse ultrices gravida. Risus commodo viverra maecenas accumsan lacus vel facilisis.iste natus error sit voluptatem accusantium doloremque laudantium, totam rem aperiam, eaque ipsa quae ab illo inventore veritatis et quasi architecto beatae vitae dicta sunt explicabo. Nemo enim ipsam voluptatem quia voluptas sit aspernatur aut.</p>
    <div class="who"><div class="avatar" role="img" aria-label="Customer portrait"></div><div><b>-Jack Marlow</b><small>Lorem Ipsum</small></div></div>
    <div class="stars">★★★★★</div>
  </article>
  <div class="vdots"><i></i><i></i><i></i><i></i></div>

  <!-- SOCIAL -->
  <h2 class="section-title" style="top:3116px">Follow Us on Social Media</h2>
  <div class="rule" style="top:3168px"></div>
  <div class="grid">
    <div class="row">
      <div role="img" aria-label="Cigar and whiskey glass on a wooden table" style="width:244px;background:linear-gradient(135deg,#3a2612,#1a1008)"></div>
      <div role="img" aria-label="Shirt cuff with a cufflink" style="width:161px;background:linear-gradient(135deg,#d8d4cc,#5a3a22 60%,#1a120a)"></div>
      <div role="img" aria-label="Chrome motorcycle engine" style="width:233px;background:linear-gradient(135deg,#8a8a8a,#2a2a2a)"></div>
      <div role="img" aria-label="Silver jewellery on wood" style="width:221px;background:linear-gradient(135deg,#8a5a24,#4a2c10)"></div>
    </div>
    <div class="row">
      <div role="img" aria-label="Wooden humidor box" style="width:190px;background:linear-gradient(135deg,#b06a30,#5a2e10)"></div>
      <div role="img" aria-label="Man adjusting a suit jacket" style="width:268px;background:linear-gradient(135deg,#2a2a2a,#0c0c0c)"></div>
      <div role="img" aria-label="Open cigar box" style="width:223px;background:linear-gradient(135deg,#c08a40,#6a4018)"></div>
      <div role="img" aria-label="Whiskey glass with smoke" style="width:178px;background:linear-gradient(135deg,#2a2420,#8a5a28)"></div>
    </div>
    <div class="row">
      <div role="img" aria-label="Red humidor being opened" style="width:244px;background:linear-gradient(135deg,#4a1a14,#1a0a08)"></div>
      <div role="img" aria-label="Black and white motorcycle detail" style="width:161px;background:linear-gradient(135deg,#e0e0e0,#1a1a1a)"></div>
      <div role="img" aria-label="Single cigar close-up" style="width:233px;background:linear-gradient(135deg,#2a3036,#5a3418 55%,#1a1410)"></div>
      <div role="img" aria-label="Row of luxury wristwatches on display" style="width:221px;background:linear-gradient(135deg,#3a2a1a,#a07a40)"></div>
    </div>
  </div>

  <!-- NEWSLETTER -->
  <section class="news">
    <h2>Subscribe to our Newsletter</h2>
    <p>Lorem ipsum dolor sit amet, consectetur adipiscing elit, sed do eiusmod tempor incididunt ut labore et dolore magna aliqua.</p>
    <div class="news-input">Enter the Email</div>
    <div class="news-btn">Subscribe Now</div>
  </section>

  <!-- FOOTER -->
  <div class="foot-brand"><span class="mark"></span>Outlaw Cupboard</div>
  <div class="foot-col" style="left:487px">
    <h4>Quick Links</h4>
    <ul>
      <li><span class="chev">»</span>Home</li>
      <li><span class="chev">»</span>About Us</li>
      <li><span class="chev">»</span>Men Products</li>
      <li><span class="chev">»</span>Categories</li>
      <li><span class="chev">»</span>Reviews</li>
      <li><span class="chev">»</span>Contact Us</li>
    </ul>
  </div>
  <div class="foot-col" style="left:650px">
    <h4>Contact Us</h4>
    <ul><li style="gap:12px"><svg width="30" height="30" viewBox="0 0 30 30"><circle cx="15" cy="15" r="15" fill="var(--gold)"/><rect x="8" y="10" width="14" height="10" fill="#fff"/><path d="M8 10l7 6 7-6" fill="none" stroke="var(--gold)" stroke-width="1.4"/></svg>info@outlawcupboard.com</li></ul>
  </div>
  <div class="foot-col social" style="left:926px">
    <h4>Follow Us</h4>
    <ul>
      <li><span class="icon-dot"></span>Facefeed</li>
      <li><span class="icon-dot"></span>Chirper</li>
      <li><span class="icon-dot"></span>Snapgram</li>
      <li><span class="icon-dot"></span>Pinboard</li>
    </ul>
  </div>
  <div class="foot-rule"></div>
  <p class="copy">© copyrights 2023 <span>Outlaw Cupboard</span> &nbsp;| &nbsp;&nbsp;&nbsp; All rights reserved.</p>

</div>
</body>
</html>
```